Bref créative
Real Estate Development Firm
Marlow Holdings
I need double sided standard sized Business Card [3.5" x 2"]
May use same font as in logo or other suggestions
Professional
Derek P. Hollins
President/CEO
248 West Penrose Street
Suite 2360
Milwaukee, WI 53217
dhollins@marlowholdingsllc.example
marlowholdingsllc.example
You can refer to logo design contest for other ideas.
Logo and design or color gradient or other suggestions.
Please use logo

```html
<!DOCTYPE html>
<html lang="en">
<head>
<meta charset="utf-8">
<title>Marlow Holdings — Business Card</title>
<link rel="stylesheet" href="https://fonts.googleapis.com/css2?family=Tinos:wght@400;700&display=swap">
<style>
  :root {
    --page: #ffffff;
    --card-front: #ffffff;
    --card-back-light: #f7f7f7;
    --card-back-dark: #d9d9d9;
    --navy: #1f2a5c;
    --ink: #2a3566;
    --mark: #3b4f8f;
    --edge: #e2e2e2;
  }
  html, body {
    margin: 0;
    width: 1200px;
    height: 338px;
    overflow: hidden;
    background: var(--page);
    font-family: "Tinos", "Times New Roman", serif;
  }
  .sheet {
    position: relative;
    width: 1200px;
    height: 338px;
  }
  .card {
    position: absolute;
    top: 5px;
    width: 566px;
    height: 328px;
    box-sizing: border-box;
    border: 1px solid var(--edge);
  }
  .card--front { left: 17px; background: var(--card-front); }
  .card--back {
    left: 617px;
    background: radial-gradient(ellipse at 50% 45%, var(--card-back-light) 0%, #ececec 55%, var(--card-back-dark) 100%);
    border-color: #d0d0d0;
  }
  .person {
    position: absolute;
    top: 12px;
    right: 22px;
    text-align: right;
    color: var(--navy);
  }
  .person__name {
    margin: 0;
    font-size: 19px;
    font-weight: 700;
    line-height: 1.15;
  }
  .person__title {
    margin: 0;
    font-size: 13px;
    line-height: 1.3;
    color: #222;
  }
  .brand {
    position: absolute;
    left: 0;
    right: 0;
    text-align: center;
    color: var(--navy);
  }
  .card--front .brand { top: 88px; }
  .card--back .brand { top: 108px; }
  .brand__dot {
    display: block;
    margin: 0 auto 14px;
    width: 44px;
    height: 44px;
  }
  .brand__name {
    margin: 0;
    font-size: 24px;
    font-weight: 400;
    letter-spacing: 1px;
    text-transform: uppercase;
    color: var(--navy);
  }
  .contact {
    position: absolute;
    left: 95px;
    top: 242px;
    margin: 0;
    padding: 0;
    list-style: none;
    font-size: 13px;
    line-height: 19px;
    color: var(--ink);
  }
</style>
</head>
<body>
<main class="sheet">
  <section class="card card--front" aria-label="Card front">
    <header class="person">
      <p class="person__name">Derek P. Hollins</p>
      <p class="person__title">President/CEO</p>
    </header>
    <div class="brand">
      <svg class="brand__dot" viewBox="0 0 44 44" aria-hidden="true"><circle cx="22" cy="22" r="20" fill="var(--mark)"/></svg>
      <p class="brand__name">Marlow Holdings</p>
    </div>
    <ul class="contact">
      <li>Add : 248 West Penrose Street Suite 2360 Milwaukee, WI 53217</li>
      <li>Ph : 414.555.0140 Cell : 414.555.0172 Fax : 414.555.0141</li>
      <li>Email : dhollins@marlowholdingsllc.example Web : marlowholdingsllc.example</li>
    </ul>
  </section>

  <section class="card card--back" aria-label="Card back">
    <div class="brand">
      <svg class="brand__dot" viewBox="0 0 44 44" aria-hidden="true"><circle cx="22" cy="22" r="20" fill="var(--mark)"/></svg>
      <p class="brand__name">Marlow Holdings</p>
    </div>
  </section>
</main>
</body>
</html>
```